Full service meeting planning company needs new business cards

Velmora Linkway is a full service meeting planning company that specializes in on-line conference registration web development and event communications. We combine citywide hotel management, mobile applications, eblast reminders, confirmation letters, and customized reporting to create a seamless registration process. We also manage group motor coach transportation, food and beverages, entertainment, stage and lighting for group of 10 to 4000.

Target Market(s)

Corporations and associations

Industry/Entity Type

Event Planning

Contact Information for Business Card

standard size 3.5" wide and 2" tall

Font styles to use
Serif
Sans Serif

Colors
f37122
f78f20
333333
5c5c5c
9d9d9d
f68d4d

Requirements
Must have
• {name}
• Velmora Linkway
• P.O. Box 7384, Grand Rapids, M I 49568
• www.velmoralinkway.com
• {email}
• {phone}
• {mobile phone}
Nice to have
• Our colors are black, grey and orange as an accent color
Should not have
• I am not happy with our website layout anymore either. It feels dark and old but it does explain who we are pretty well if you'd like to review; www.velmoralinkway.com

```html
<!DOCTYPE html>
<html lang="en">
<head>
<meta charset="utf-8">
<title>Velmora Linkway – Business Card</title>
<link rel="stylesheet" href="https://fonts.googleapis.com/css2?family=Montserrat:wght@600&family=Open+Sans:wght@400&display=swap">
<style>
  :root {
    --orange-deep: #f37122;
    --orange: #f78f20;
    --orange-soft: #f0a23e;
    --charcoal: #333333;
    --grey-dark: #5c5c5c;
    --grey-light: #9d9d9d;
    --paper: #e6e6e6;
    --white: #ffffff;
  }
  * { margin: 0; padding: 0; box-sizing: border-box; }
  html, body {
    width: 1200px;
    height: 900px;
    overflow: hidden;
    background: var(--paper);
  }
  .stage {
    position: relative;
    width: 1200px;
    height: 900px;
    display: flex;
    align-items: center;
    justify-content: center;
  }
  .business-card {
    position: relative;
    width: 1050px;
    height: 600px;
    overflow: hidden;
    background: radial-gradient(ellipse at 60% 35%, var(--orange-soft) 0%, var(--orange) 55%, var(--orange-deep) 100%);
  }
  .edge-block-left {
    position: absolute;
    left: 0;
    top: 300px;
    width: 95px;
    height: 95px;
    background: var(--charcoal);
  }
  .edge-steps-right {
    position: absolute;
    right: 0;
    top: 120px;
    width: 190px;
    height: 230px;
  }
  .brand-lockup {
    position: absolute;
    left: 130px;
    top: 175px;
    display: flex;
    align-items: center;
    gap: 36px;
  }
  .brand-mark {
    width: 220px;
    height: 220px;
    border-radius: 50%;
    background: var(--white);
    flex: none;
  }
  .brand-text {
    display: flex;
    flex-direction: column;
    align-items: flex-end;
    gap: 8px;
    max-width: 460px;
  }
  .brand-name {
    font-family: "Montserrat", sans-serif;
    font-weight: 600;
    font-size: 40px;
    letter-spacing: 1px;
    text-transform: uppercase;
    color: var(--white);
    white-space: nowrap;
  }
  .brand-url {
    font-family: "Open Sans", sans-serif;
    font-weight: 400;
    font-size: 20px;
    letter-spacing: 0.5px;
    color: var(--white);
    white-space: nowrap;
  }
</style>
</head>
<body>
  <main class="stage">
    <section class="business-card" aria-label="Velmora Linkway business card, front">
      <div class="edge-block-left"></div>
      <svg class="edge-steps-right" viewBox="0 0 190 230" aria-hidden="true">
        <polygon points="0,0 60,0 60,40 100,40 100,85 150,85 150,150 190,150 190,230 150,230 150,190 100,190 100,130 60,130 60,95 0,95" fill="var(--charcoal)"/>
      </svg>
      <div class="brand-lockup">
        <div class="brand-mark" aria-hidden="true"></div>
        <div class="brand-text">
          <h1 class="brand-name">Velmora Linkway</h1>
          <p class="brand-url">www.velmoralinkway.com</p>
        </div>
      </div>
    </section>
  </main>
</body>
</html>
```